Gordon Pellbrook Consulting - Web Design Project

We need a web design for my new edgy consulting business specializing in innovation, technology and strategy.

It is our personal goal to turn each client into raving fans by helping them achieve their own business goals and aspirations through assisting them in raising their own innovation and marketing standards.

We provide our personalised and state-of-the-art services to our clients and boards who represent some of the world greatest innovative thinkers.
Updates

Here is some other information which may help shape your thinking.

I've had direct Involvement in the development of the following iPad, iPhone Applications and websites

FarbeyondOzlands.com (TerraLink platform) by Voyage Bureau
http://farbeyondozlands.example.au

Sail Verve by Bright Voyaging
https://apps.example-store.com/au/app/sail-verve/id100000001

uRedlandTR by Travel Territory Board
https://apps.example-store.com/au/app/uredlandtr/id100000002

Wexmoor Trips
http://www.wexmoortrips.example.au

Trek Mapper by Voyage Bureau
http://apps.example-store.com/au/app/trek-mapper/id100000003

Sunward by Sunward Travel Office
https://apps.example-store.com/au/app/sunward/id100000004

Upper Fernridge Valley Route by Visit Coastlands
https://apps.example-store.com/au/app/upper-fernridge-valley-route/id100000005

Wanderer Path by Travel Territory Board and Southern Plains Travel Council
https://apps.example-store.com/au/app/wanderers-path-grand-journey/id100000006

Gordon Pellbrook Consulting (GPC)
November 2012 – Present (8 months)Brisbane, Sydney, Canberra

Gordon’s consults to Small-to-Medium Enterprises (SME) and Government organisations on business strategy, technology strategy, risk mitigation, disruptive technology and innovation in the workplace.

Gordon’s consultancy mantra is that we cannot divorce economic life from cultural life particularly in an era when social capital may be as important as physical capital in business.

Reason: request from designers, I want to see their best efforts

Target Market(s)

35+

Industry/Entity Type

Business

Requirements
Must have
• Please use some of the personal image(s) contained in the zip files which can be downloaded from here

http://filedrop.example/k9Xq2Lm
http://filedrop.example/p4Rt7Vn
http://filedrop.example/z8Hw3Bc
Nice to have
• Black, Sleek design, maybe minimalist. Nice to have a Pixelle for the design. Nice to have it easily ported to Wordpress or be a modified Wordpress template. HTML 5, responsive design

```html
<!DOCTYPE html>
<html lang="en">
<head>
<meta charset="utf-8">
<title>Gordon Pellbrook Consulting</title>
<link rel="stylesheet" href="https://fonts.googleapis.com/css2?family=Raleway:wght@400;500&family=Source+Sans+3:wght@400;600&display=swap">
<style>
:root{
  --navy:#13134a;
  --white:#ffffff;
  --page-grey:#5e5e5e;
  --footer:#2b2b2b;
  --card-dark:#2a2a2a;
  --tab-grey:#6b6b6b;
  --text:#1d1d1d;
  --light:#e8e8e8;
}
*{margin:0;padding:0;box-sizing:border-box}
html,body{width:987px;height:1200px;overflow:hidden}
body{position:relative;background:var(--page-grey);font-family:"Source Sans 3",sans-serif;color:var(--text)}
.abs{position:absolute}
.header{left:0;top:0;width:987px;height:86px;background:var(--white)}
.header-rule{left:0;top:86px;width:987px;height:8px;background:var(--navy)}
.brand{left:89px;top:0;width:171px;height:86px;background:var(--navy);color:var(--white);text-align:center}
.brand-mark{font-family:"Raleway",sans-serif;font-weight:500;font-size:58px;line-height:66px;letter-spacing:-2px}
.brand-name{font-family:"Source Sans 3",sans-serif;font-size:8.5px;letter-spacing:.2px;margin-top:2px}
.nav a{position:absolute;top:63px;height:23px;line-height:25px;font-size:11px;color:#111;text-decoration:none}
.nav .active{background:var(--navy);color:var(--white);padding:0 9px;left:475px}
.hero{left:0;top:94px;width:987px;height:405px;background:linear-gradient(100deg,#7a7a7a 0%,#c9c9c9 22%,#9d9d9d 45%,#8a8a8a 70%,#b5b5b5 100%)}
.hero-box{left:297px;top:179px;width:391px;height:165px;background:rgba(19,19,74,.92);color:var(--white);text-align:center;font-family:"Raleway",sans-serif}
.hero-title{font-size:39px;line-height:44px;margin-top:12px}
.hero-sub{font-size:24px;line-height:29.5px;margin-top:4px}
.frame{left:101px;top:410px;width:782px;height:606px;background:var(--navy)}
.panel{left:120px;top:426px;width:744px;height:573px;background:var(--white)}
.section-title{left:120px;width:744px;text-align:center;font-family:"Raleway",sans-serif;font-size:26px;color:var(--navy);line-height:30px}
.copy{left:168px;width:652px;font-size:12.3px;line-height:15px}
.tab{height:24px;background:#f1f1f1;border:1px solid #bbb;font-family:"Raleway",sans-serif;font-size:11px;color:#333;text-align:center;line-height:22px;box-shadow:1px 1px 2px rgba(0,0,0,.4)}
.partner{top:730px;width:89px;height:88px;background:var(--navy)}
.news-head{top:878px;width:185px;height:19px;background:var(--tab-grey);color:var(--white);font-family:"Raleway",sans-serif;font-size:11px;text-align:center;line-height:19px}
.news-body{top:900px;width:185px;height:84px;background:var(--card-dark);color:var(--light);font-size:9.6px;line-height:12px;padding:5px 10px}
.footer{left:0;top:1042px;width:987px;height:158px;background:var(--footer)}
.foot-links a{position:absolute;left:141px;font-size:10.5px;color:var(--white);text-decoration:none}
.news-title{left:428px;top:1055px;width:130px;font-size:11px;color:var(--white);text-align:center}
.news-input{left:428px;top:1075px;width:129px;height:21px;background:var(--white)}
.privacy{left:442px;top:1103px;width:120px;font-size:7px;line-height:9px;color:#ccc}
.signup{left:468px;top:1127px;width:49px;height:16px;background:var(--navy);color:var(--white);font-size:11px;text-align:center;line-height:16px}
.social{left:712px;top:1070px;width:140px;display:flex;justify-content:space-between;font-size:9px;color:var(--white)}
.address{left:703px;top:1102px;width:160px;text-align:center;font-size:10.5px;line-height:13.2px;color:var(--white)}
.legal{left:343px;top:1164px;width:300px;text-align:center;font-size:8.5px;line-height:11px;color:var(--white)}
</style>
</head>
<body>
<header class="abs header"></header>
<div class="abs header-rule"></div>
<div class="abs brand">
  <div class="brand-mark">GPC</div>
  <div class="brand-name">GORDON PELLBROOK CONSULTING</div>
</div>
<nav class="nav">
  <a class="active" href="#">HOME</a>
  <a href="#" style="left:582px">ABOUT US</a>
  <a href="#" style="left:701px">CLIENTS</a>
  <a href="#" style="left:812px">CONTACT US</a>
</nav>

<div class="abs hero" role="img" aria-label="Black and white photo of a coin-operated viewing telescope overlooking a city and river"></div>
<div class="abs hero-box">
  <div class="hero-title">Business Consulting</div>
  <div class="hero-sub">innovation<br>technology<br>strategy</div>
</div>

<div class="abs frame"></div>
<main class="abs panel"></main>

<h2 class="abs section-title" style="top:440px">Welcome to GPC</h2>
<p class="abs copy" style="top:479px">Lorem ipsum dolor sit amet, consectetur adipisicing elit, sed do eiusmod tempor incididunt ut labore et dolore magna aliqua. Ut enim ad minim veniam, quis nostrud exercitation ullamco laboris nisi ut aliquip ex ea commodo consequat. Duis aute irure dolor in reprehenderit in voluptate velit esse cillum dolore eu fugiat nulla pariatur. Excepteur sint occaecat cupidatat non proident, sunt in culpa qui officia deserunt mollit anim id est laborum.</p>
<div class="abs tab" style="left:823px;top:498px;width:65px">read more</div>

<h2 class="abs section-title" style="top:566px">Our Competitive Advantage</h2>
<p class="abs copy" style="top:605px">Lorem ipsum dolor sit amet, consectetur adipisicing elit, sed do eiusmod tempor incididunt ut labore et dolore magna aliqua. Ut enim ad minim veniam, quis nostrud exercitation ullamco laboris nisi ut aliquip ex ea commodo consequat. Duis aute irure dolor in reprehenderit in voluptate velit esse cillum dolore eu fugiat nulla pariatur. Excepteur sint occaecat cupidatat non proident, sunt in culpa qui officia deserunt mollit anim id est laborum.</p>

<h2 class="abs section-title" style="top:692px">Recent Partners</h2>
<div class="abs partner" style="left:190px"></div>
<div class="abs partner" style="left:293px"></div>
<div class="abs partner" style="left:396px"></div>
<div class="abs partner" style="left:499px"></div>
<div class="abs partner" style="left:602px"></div>
<div class="abs partner" style="left:705px"></div>
<div class="abs tab" style="left:836px;top:762px;width:52px">view all</div>

<h2 class="abs section-title" style="top:842px">Latest News</h2>
<div class="abs news-head" style="left:171px">New Business Deal for Company</div>
<div class="abs news-head" style="left:400px">New Business Deal for Company</div>
<div class="abs news-head" style="left:629px">New Business Deal for Company</div>
<div class="abs news-body" style="left:171px">Lorem ipsum dolor sit amet, consectetur adipisicing elit, sed do eiusmod tempor incididunt ut labore et dolore magna aliqua. Ut enim ad minim veniam, quis nostrud exercitation ullamco laboris nisi ut aliquip ex ea commodo consequat.</div>
<div class="abs news-body" style="left:400px">Lorem ipsum dolor sit amet, consectetur adipisicing elit, sed do eiusmod tempor incididunt ut labore et dolore magna aliqua. Ut enim ad minim veniam, quis nostrud exercitation ullamco laboris nisi ut aliquip ex ea commodo consequat.</div>
<div class="abs news-body" style="left:629px">Lorem ipsum dolor sit amet, consectetur adipisicing elit, sed do eiusmod tempor incididunt ut labore et dolore magna aliqua. Ut enim ad minim veniam, quis nostrud exercitation ullamco laboris nisi ut aliquip ex ea commodo consequat.</div>
<div class="abs tab" style="left:823px;top:932px;width:65px">read more</div>

<footer class="abs footer"></footer>
<nav class="foot-links">
  <a href="#" style="top:1059px">HOME</a>
  <a href="#" style="top:1080px">ABOUT US</a>
  <a href="#" style="top:1100px">CLIENTS</a>
  <a href="#" style="top:1121px">CONTACT US</a>
</nav>
<div class="abs news-title">Sign Up for our Newsletter</div>
<div class="abs news-input"></div>
<svg class="abs" style="left:428px;top:1106px" width="10" height="12" viewBox="0 0 10 12"><path d="M2.5 5V3.5a2.5 2.5 0 0 1 5 0V5" fill="none" stroke="#fff" stroke-width="1.3"/><rect x="1" y="5" width="8" height="6.5" fill="#fff"/></svg>
<div class="abs privacy">Your data is strictly private and will be used only for the above purpose</div>
<div class="abs signup">sign up</div>
<div class="abs social"><span>Circlet</span><span>Murmur</span><span>Linkway</span><span>Orbitly</span></div>
<div class="abs address">Brevant Holdings<br>XXX Street 216<br>City<br>State<br>Post Code</div>
<div class="abs legal">Copyright © 2013 GPC GORDON PELLBROOK CONSULTING<br>Terms Of Use</div>
</body>
</html>
```